Clean-tech company needs graphic showing how they help with energy savings*

We need a new graphic showing how we help customers save energy and money with our product. It's one of the most important things to convey to our customers, but we still don't have our own graphic detailing this solution to the customer. It's a simple task, and a simple overview, showing how we can balance out the temperature in any large facility, with our large ceiling fan. <br/> <br/>HOW IT WORKS:<br/>Normally in any large facility, when heating it up, the hot air rises to the ceiling, and you have a colder temperature at the bottom of the room. When we use our product, we are able to mix that temperature up, meaning that there is the same temperature in the whole room. This is known as “destratification” – and lets the building manager reduce his energy consumption, as he now doesn't have to heat his building so much. <br/> <br/>We would like to have a side-by-side comparison, before using our product, and after (I have attached photos of similar graphics). Maybe the title of the two graphics should be “WITHOUT HVLS FAN” and “WITH HVLS FAN”. As our main product is a very big (HVLS) ceiling fan, it is essential that in the second picture that shows the balanced temperature, that there is a fan in the picture to illustrate that it is the product that does this.<br/> <br/>As we are a European company, we use CELSIU (°C). Like in the photos attached, it is good to show two different temperatures, at floor and ceiling level. In the first picture, this could be 17 degrees at the floor level, and 23 degrees at the ceiling level. Then in the next picture, with a fan hanging from the ceiling, it could show that there is a temperature of 20 degrees at the bottom, and a temperature of 20 in the ceiling. (Please look at files attached for reference points). <br/> <br/>We would like to have a simple design (less-is-more) and have it match our current company colors and design, which you can see on our website and below, www.halvorbreezeworks.com<br/>The most important colors have the following color codes: <br/><br/>Color 1: Hex: #53c0ab RGB: 83,192,171 CMYK: 64,0,41,0.<br/>Color 2: Hex: #3c3c3b RGB: 60,60,59 CMYK: 0,0,0,90<br/>Color 3: Hex: #727677 RGB: 114,118,119 CMYK: 27,17,18,54<br/>And regarding fonts, we use:<br/><br/>Font: Avenir, Usage: Body text, Headlines, Content elements Font-size: Variable<br/>Font: Bebas Neue Usage: Headlines Font-size: Variable<br/>Font: Nunito, Usage: Web body text, Web headlines, Web content elements<br/>Font-size: Variable<br/><br/><br/><br/>IT SHOULD BE NOTED THAT OUR FAVORITE ILLUSTRATION OF THE THREE ATTACHED, IS THE THIRD, ILLUSTRATING HOT AIR RISES, AND WHERE IT SAYS WITHOUT A LUMO KITE FAN, AND WITH A LUMO KITE FAN.
Customers include factories, manufacturers, distribution centers, warehouses, etc.
- Font: Avenir, Usage: Body text, Headlines, Content elements Font-size: Variable Font: Bebas Neue Usage: Headlines Font-size: Variable Font: Nunito, Usage: Web body text, Web headlines, Web content elements Font-size: Variable

```html
<!DOCTYPE html>
<html lang="en">
<head>
<meta charset="utf-8">
<title>Halvor Breezeworks – Destratification</title>
<link rel="stylesheet" href="https://fonts.googleapis.com/css2?family=Bebas+Neue&family=Nunito:wght@400;600;700&display=swap">
<style>
  :root{
    --teal:#53c0ab;
    --teal-deep:#3f9c8a;
    --charcoal:#3c3c3b;
    --slate:#727677;
    --white:#ffffff;
    --stage:#e4e4e4;
    --pill-light:#9a9d9e;
    --pill-dark:#5b5e5f;
  }
  *{box-sizing:border-box;margin:0;padding:0}
  html,body{width:1200px;height:940px;overflow:hidden}
  body{background:var(--stage);position:relative;font-family:"Nunito",sans-serif}

  .banner{position:absolute;left:40px;top:212px;width:1120px;height:516px;background:var(--white)}

  .brand{position:absolute;top:28px;left:0;width:100%;display:flex;justify-content:center;align-items:center;gap:10px}
  .brand-dot{width:34px;height:34px;border-radius:50%;background:var(--charcoal)}
  .brand-name{font-weight:700;font-size:17px;color:var(--charcoal);letter-spacing:.2px;line-height:1}
  .brand-tagline{font-size:9.5px;color:var(--charcoal);letter-spacing:.4px;margin-top:4px}

  .column-title{position:absolute;top:78px;width:200px;text-align:center;color:var(--charcoal)}
  .column-title--without{left:179px}
  .column-title--with{left:741px}
  .column-title strong{display:block;font-family:"Bebas Neue",sans-serif;font-weight:400;font-size:35px;line-height:30px;text-shadow:1px 1px 1px rgba(0,0,0,.2)}
  .column-title span{display:block;font-size:15px;line-height:18px;color:var(--charcoal)}

  .header-divider{position:absolute;left:558px;top:82px;width:2px;height:52px;background:var(--slate)}
  .band{position:absolute;left:0;width:100%;height:6px;background:var(--charcoal)}
  .band--top{top:139px}
  .band--bottom{top:500px}

  .panel{position:absolute;top:145px;height:355px}
  .panel--without{left:0;width:558px;background:linear-gradient(to bottom,var(--teal) 0%,#a9dfd3 45%,#f4fbf9 100%)}
  .panel--with{left:561px;width:559px;background:var(--teal)}
  .panel-divider{position:absolute;left:558px;top:145px;width:3px;height:355px;background:var(--slate)}

  .art{position:absolute;left:0;top:0;width:1120px;height:516px;pointer-events:none}

  .rise-label{position:absolute;left:361px;top:333px;transform:translate(-50%,-50%) rotate(-90deg);font-family:"Bebas Neue",sans-serif;font-size:40px;line-height:1;color:var(--charcoal);white-space:nowrap;letter-spacing:.5px}

  .fan-figure{position:absolute;left:611px;top:145px;width:320px;height:127px;border-radius:0 0 60px 60px;background:linear-gradient(to bottom,rgba(60,60,59,.35),rgba(60,60,59,.12))}

  .temp-badge{position:absolute;width:182px;height:80px}
  .temp-badge--ceiling-cold{left:24px;top:175px}
  .temp-badge--floor-cold{left:26px;top:389px}
  .temp-badge--ceiling-even{left:939px;top:175px}
  .temp-badge--floor-even{left:939px;top:389px}
  .badge-pill{position:absolute;left:38px;top:14px;width:118px;height:52px;border-radius:0 26px 26px 0;background:linear-gradient(to bottom,var(--pill-light),var(--pill-dark));border:2px solid var(--charcoal);padding-left:36px;text-align:center;color:var(--white);font-family:"Bebas Neue",sans-serif;box-shadow:1px 2px 3px rgba(0,0,0,.25)}
  .badge-pill small{display:block;font-size:13px;line-height:13px;margin-top:5px}
  .badge-pill b{display:block;font-weight:400;font-size:23px;line-height:22px}
  .badge-dial{position:absolute;left:0;top:0;width:80px;height:80px;border-radius:50%;background:var(--white);border:5px solid var(--teal);box-shadow:0 0 0 2px var(--charcoal),1px 2px 4px rgba(0,0,0,.3);display:flex;align-items:center;justify-content:center;font-family:"Bebas Neue",sans-serif;font-size:42px;color:var(--charcoal);padding-top:3px}
</style>
</head>
<body>
<section class="banner">
  <header class="brand">
    <div class="brand-dot"></div>
    <div>
      <div class="brand-name">HALVOR BREEZEWORKS</div>
      <div class="brand-tagline">SILENT &bull; CLIMATE-FRIENDLY &bull; COMFORT</div>
    </div>
  </header>

  <h2 class="column-title column-title--without"><strong>WITHOUT</strong><span>HALVOR FAN</span></h2>
  <div class="header-divider"></div>
  <h2 class="column-title column-title--with"><strong>WITH</strong><span>HALVOR FAN</span></h2>

  <div class="band band--top"></div>
  <div class="panel panel--without"></div>
  <div class="panel panel--with"></div>
  <div class="panel-divider"></div>
  <div class="band band--bottom"></div>

  <svg class="art" viewBox="0 0 1120 516" aria-hidden="true">
    <defs>
      <linearGradient id="shaftFade" x1="0" y1="0" x2="0" y2="1">
        <stop offset="0" stop-color="#ffffff" stop-opacity="1"/>
        <stop offset="0.8" stop-color="#ffffff" stop-opacity=".9"/>
        <stop offset="1" stop-color="#ffffff" stop-opacity="0"/>
      </linearGradient>
      <marker id="head" viewBox="0 0 10 10" refX="3" refY="5" markerWidth="3.4" markerHeight="3.4" orient="auto">
        <path d="M0 0 L10 5 L0 10 Z" fill="#ffffff"/>
      </marker>
    </defs>
    <!-- rising air arrow -->
    <path d="M361 166 L424 235 L399 235 L399 470 L322 470 L322 235 L297 235 Z" fill="url(#shaftFade)"/>
    <path d="M314 250 C306 320 318 380 308 470" stroke="#ffffff" stroke-opacity=".7" stroke-width="2" fill="none"/>
    <path d="M407 250 C415 320 403 380 412 470" stroke="#ffffff" stroke-opacity=".7" stroke-width="2" fill="none"/>

    <!-- circulation arrows -->
    <g stroke="#ffffff" stroke-width="6" fill="none" stroke-linecap="round" marker-end="url(#head)">
      <path d="M605 354 Q592 320 601 296"/>
      <path d="M937 351 Q950 320 944 296"/>
      <path d="M712 320 Q692 314 681 298"/>
      <path d="M834 320 Q854 314 865 298"/>
      <path d="M758 286 Q752 308 737 320"/>
      <path d="M788 286 Q794 308 809 320"/>
      <path d="M689 412 Q652 404 632 382"/>
      <path d="M857 412 Q894 404 914 382"/>
      <path d="M754 366 Q745 395 718 412"/>
      <path d="M792 366 Q801 395 828 412"/>
    </g>
  </svg>

  <div class="rise-label">HOT AIR RISES</div>
  <div class="fan-figure" role="img" aria-label="Large HVLS ceiling fan hanging from the ceiling"></div>

  <div class="temp-badge temp-badge--ceiling-cold">
    <div class="badge-pill"><small>AT THE</small><b>CEILING</b></div>
    <div class="badge-dial">23°</div>
  </div>
  <div class="temp-badge temp-badge--floor-cold">
    <div class="badge-pill"><small>AT THE</small><b>FLOOR</b></div>
    <div class="badge-dial">17°</div>
  </div>
  <div class="temp-badge temp-badge--ceiling-even">
    <div class="badge-pill"><small>AT THE</small><b>CEILING</b></div>
    <div class="badge-dial">20°</div>
  </div>
  <div class="temp-badge temp-badge--floor-even">
    <div class="badge-pill"><small>AT THE</small><b>FLOOR</b></div>
    <div class="badge-dial">20°</div>
  </div>
</section>
</body>
</html>
```